Re-Design of existing Shopify Website

Hi,

We are looking for a skilled person to work with us on improving the design of our website to make it more user friendly. We are a Makeup brush and makeup accessories company and our current website can be viewed at lumeandwisp dot com.We are looking to simplify the layout and make it more modern and mobile friendly.

We have designs in mind which we would like to implement to our site which we feel would work better for us to increase traffic and sales.

We would like the layout to have clear sections for brushes,lashes ,sponge and also our tutorials on the landing page.

Industry/Entity Type

Hair And Beauty

Number of Pages Required

5+ page

Font styles to use
Sans Serif

Colors
b8a6cd
d3a5cc
eea4c8
ffffff
000000

Requirements
Must have
• -Clear ,modern landing page.
• -easy navigation
• -simple design
• -professional design approach
Nice to have
• cross selling pop up
Should not have
• over use of bold colour.

```html
<!DOCTYPE html>
<html lang="en">
<head>
<meta charset="utf-8">
<title>Lume &amp; Wisp — Makeup Brushes &amp; Accessories</title>
<link href="https://fonts.googleapis.com/css2?family=Montserrat:wght@400;500;600;700&family=Mulish:wght@400;600&display=swap" rel="stylesheet">
<style>
:root{
  --pink:#ee8fb8;
  --pink-soft:#f4bfd6;
  --pink-band:#f09fc3;
  --pink-text:#ee86b4;
  --teal:#5fc3cd;
  --ink:#1c1c1c;
  --body:#555;
  --grey-bg:#f1f1f1;
  --footer-bg:#d9d9d9;
  --orange:#e8644a;
  --gold:#c9a13b;
  --white:#fff;
}
*{box-sizing:border-box;margin:0;padding:0}
html,body{width:1200px;height:3354px;overflow:hidden}
body{position:relative;background:var(--white);font-family:'Mulish',sans-serif;color:var(--body)}
.abs{position:absolute}

/* hero */
.hero{left:0;top:0;width:1200px;height:624px;background:linear-gradient(100deg,#e4cabe 0%,#efdbd2 50%,#e8d3cc 100%)}
.logo{left:22px;top:22px;font-family:'Montserrat',sans-serif;font-weight:500;font-size:28px;line-height:1;color:var(--pink);letter-spacing:.5px}
.nav{left:470px;top:38px;display:flex;gap:34px;align-items:center;font-family:'Montserrat',sans-serif;font-size:12px;font-weight:500;color:var(--white);letter-spacing:.5px}
.nav .dot{width:14px;height:14px;border-radius:50%;background:var(--gold)}
.hero-copy{left:430px;top:232px;width:330px;text-align:center;font-family:'Montserrat',sans-serif}
.hero-copy .lead{font-size:42px;font-weight:400;color:var(--ink);line-height:1.1}
.hero-copy .line{font-size:27px;font-weight:600;color:var(--ink);letter-spacing:1.5px;line-height:34px}
.hero-copy .accent{color:var(--teal);font-weight:400}
.slider-dot{left:1005px;top:472px;width:12px;height:12px;border-radius:50%;background:var(--gold)}

/* category tiles */
.tile{top:624px;width:400px;height:227px;display:flex;flex-direction:column;align-items:center;justify-content:center;font-family:'Montserrat',sans-serif;text-align:center}
.tile-brushes{left:0;background:linear-gradient(90deg,#e9e4e0,#f6f3f1)}
.tile-lashes{left:400px;background:#1e1e1e;border:8px solid #555}
.tile-sponge{left:800px;background:linear-gradient(90deg,#efe6e1,#f5ece8);padding-bottom:30px}
.tile .kicker{font-size:14px;font-weight:500;letter-spacing:1px}
.tile .name{font-size:40px;font-weight:600;letter-spacing:1px;line-height:1.1}
.tile-brushes .name,.tile-sponge .name,.tile-sponge .kicker{color:#3a2a2a}
.tile-brushes .kicker{color:#777;order:2;font-size:12px}
.tile-lashes .name,.tile-lashes .kicker{color:var(--white)}
.tile .shop{margin-top:10px;border:2px solid var(--orange);color:var(--orange);font-size:10px;padding:4px 16px;letter-spacing:1px}

/* about */
.about-photo{left:206px;top:890px;width:329px;height:491px;background:linear-gradient(160deg,#3c3a3d 0%,#5a4f58 50%,#2a2729 100%)}
.about-title{left:610px;top:1020px;font-family:'Montserrat',sans-serif;font-size:33px;font-weight:500;line-height:42px;color:var(--pink-text)}
.about-text{left:610px;top:1128px;width:430px;font-size:14.5px;line-height:23px;color:#444}
.btn-pill{left:610px;top:1241px;width:202px;height:46px;border-radius:23px;background:var(--pink);color:var(--white);font-family:'Montserrat',sans-serif;font-weight:600;font-size:14px;display:flex;align-items:center;justify-content:center;letter-spacing:.5px}

/* beauty band */
.band{left:0;top:1422px;width:1200px;height:471px;background:linear-gradient(180deg,#e08fb2 0%,var(--pink-band) 40%,var(--pink-band) 100%)}
.band-title{left:330px;top:1597px;width:540px;text-align:center;font-family:'Montserrat',sans-serif;font-size:31px;letter-spacing:2px;line-height:38px;color:var(--ink)}
.band-title b{font-weight:700}
.band-title span{font-weight:400}
.band-text{left:370px;top:1703px;width:460px;text-align:center;font-size:12.5px;line-height:19px;color:#5a3b48}
.btn-outline{left:539px;top:1796px;width:165px;height:41px;border:2px solid var(--orange);color:var(--orange);font-family:'Montserrat',sans-serif;font-size:12px;font-weight:600;display:flex;align-items:center;justify-content:center;letter-spacing:1px}

/* tutorials */
.tutorials{left:0;top:1893px;width:1200px;height:734px;background:var(--grey-bg)}
.tut-title{left:0;top:1958px;width:1200px;text-align:center;font-family:'Montserrat',sans-serif;font-size:31px;font-weight:600;color:var(--pink-text)}
.tut-text{left:370px;top:2018px;width:460px;text-align:center;font-size:15px;line-height:24px;color:#444}
.video{left:303px;top:2108px;width:592px;height:360px;border-radius:6px;background:linear-gradient(135deg,#a8958e 0%,#c4b2ab 50%,#9c8982 100%);box-shadow:0 20px 40px rgba(0,0,0,.2)}
.play{left:540px;top:2232px}
.arrows{left:572px;top:2510px}

/* instagram */
.insta-strip{left:0;top:2627px;width:1200px;height:183px;display:flex}
.insta-strip div{flex:1;height:183px}
.handle-bar{left:0;top:2810px;width:1200px;height:53px;background:var(--pink);border:2px solid #f7a98a;display:flex;align-items:center;justify-content:center;gap:8px;color:var(--white);font-size:16px}
.handle-bar .sq{width:16px;height:16px;border:2px solid var(--white);border-radius:4px}

/* newsletter */
.newsletter{left:0;top:2863px;width:1200px;height:165px;background:var(--pink-soft)}
.news-title{left:145px;top:2913px;font-family:'Montserrat',sans-serif;font-size:17px;font-weight:600;letter-spacing:1px;color:var(--white)}
.news-text{left:145px;top:2943px;width:380px;font-size:11.5px;line-height:17px;color:#fbe3ee}
.news-input{left:707px;top:2920px;width:351px;height:46px;background:rgba(255,255,255,.35)}
.news-arrow{left:1010px;top:2935px}

/* footer */
.footer{left:0;top:3028px;width:1200px;height:223px;background:var(--footer-bg)}
.footer-logo{left:0;top:3110px;width:1200px;text-align:center;font-family:'Montserrat',sans-serif;font-weight:500;font-size:32px;line-height:40px;color:var(--pink)}
.footer-links{left:0;top:3225px;width:1200px;display:flex;justify-content:center;gap:28px;font-family:'Montserrat',sans-serif;font-size:10.5px;letter-spacing:.6px;color:#666}
.social{left:0;top:3268px;width:1200px;display:flex;justify-content:center;gap:22px}
.social span{width:16px;height:16px;border-radius:50%;background:var(--gold)}
.rule{left:0;top:3315px;width:1200px;height:1px;background:#ddd}
.copyright{left:0;top:3327px;width:1200px;text-align:center;font-size:9.5px;color:#555}
</style>
</head>
<body>

<header>
  <div class="abs hero" role="img" aria-label="Close-up of a model with bright eyeshadow and pink lips, a hand applying shadow with a brush"></div>
  <div class="abs logo">Lume &amp; Wisp</div>
  <nav class="abs nav">
    <span>SHOP</span><span>ABOUT US</span><span>CONTACT US</span><span>MY BOOKING</span><span>LOGIN</span><span class="dot"></span>
    <svg width="14" height="14" viewBox="0 0 14 14"><circle cx="6" cy="6" r="4.5" fill="none" stroke="#fff" stroke-width="1.5"/><line x1="9.5" y1="9.5" x2="13" y2="13" stroke="#fff" stroke-width="1.5"/></svg>
    <svg width="14" height="14" viewBox="0 0 14 14"><path d="M2 5h10l-1 8H3z" fill="none" stroke="#fff" stroke-width="1.4"/><path d="M5 5V3a2 2 0 0 1 4 0v2" fill="none" stroke="#fff" stroke-width="1.4"/></svg>
  </nav>
  <div class="abs hero-copy">
    <div class="lead">We are</div>
    <div class="line">MAKEUP BRUSH</div>
    <div class="line"><span class="accent">AND</span> MAKEUP</div>
    <div class="line">ACCESSORIES</div>
    <div class="line accent">COMPANY</div>
  </div>
  <div class="abs slider-dot"></div>
</header>

<section>
  <div class="abs tile tile-brushes" role="img" aria-label="Model holding a fan of makeup brushes"><div class="name">BRUSHES</div><div class="kicker">BIG SALE</div></div>
  <div class="abs tile tile-lashes" role="img" aria-label="Model applying mascara to her lashes"><div class="kicker">NEW TREND</div><div class="name">LASHES</div><div class="shop">SHOP NOW</div></div>
  <div class="abs tile tile-sponge" role="img" aria-label="Model holding a pink makeup sponge"><div class="kicker">NEW TREND</div><div class="name">SPONGE</div></div>
</section>

<section>
  <div class="abs about-photo" role="img" aria-label="Portrait of a model with smoky purple eye makeup"></div>
  <h2 class="abs about-title">A Few Words About<br>Our Company</h2>
  <p class="abs about-text">Lorem ipsum dolor sit amet, consectetuer adipiscing elit, sed diam nonummy nibh euismod tincidunt ut laoreet dolore magna aliquam erat volutpat wisi enim ad minim veniam, quis nostrud exerci tation ullamcorper suscipit lobortis.</p>
  <div class="abs btn-pill">SHOW MORE</div>
</section>

<section>
  <div class="abs band" role="img" aria-label="Flat lay of brushes, lipstick, compacts, blush, glasses and a powder puff on pink"></div>
  <h2 class="abs band-title"><b>EVERYTHING HAS</b> <span>BEAUTY</span><br><b>MAKE UP IS</b> <span>ART</span></h2>
  <p class="abs band-text">Duis autem vel eum iriure dolor in hendrerit in vulputate velit esse molestie consequat, vel illum dolore eu feugiat nulla facilisis at vero eros et accumsan et iusto odio dignissim qui blandit praesent luptatum.</p>
  <div class="abs btn-outline">LEARN MORE</div>
</section>

<section>
  <div class="abs tutorials"></div>
  <h2 class="abs tut-title">Watch Our Video Tutorials</h2>
  <p class="abs tut-text">Investigationes demonstraverunt lectores legere me lius quod ii legunt saepius. Claritas est etiam processus dynamicus.</p>
  <div class="abs video" role="img" aria-label="Video tutorial still of a model applying red lipstick"></div>
  <svg class="abs play" width="120" height="120" viewBox="0 0 120 120"><circle cx="60" cy="60" r="51" fill="rgba(0,0,0,.15)" stroke="#fff" stroke-width="4"/><path d="M49 40l32 20-32 20z" fill="#fff"/></svg>
  <svg class="abs arrows" width="56" height="24" viewBox="0 0 56 24"><path d="M14 3l-9 9 9 9" fill="none" stroke="#bbb" stroke-width="2.5"/><path d="M40 3l9 9-9 9" fill="none" stroke="#3d6e8c" stroke-width="2.5"/></svg>
</section>

<section>
  <div class="abs insta-strip">
    <div role="img" aria-label="Instagram photo of pastel eye makeup" style="background:#e6e3e5"></div>
    <div role="img" aria-label="Instagram photo of a model with a brush" style="background:#caa79a"></div>
    <div role="img" aria-label="Instagram photo of a red-haired model with brushes" style="background:#d98a72"></div>
    <div role="img" aria-label="Instagram photo of a model with an oval brush" style="background:#6e5449"></div>
    <div role="img" aria-label="Instagram photo of a model with curly hair applying mascara" style="background:#8b6a52"></div>
    <div role="img" aria-label="Instagram photo of a model applying makeup" style="background:#eee9e7"></div>
    <div role="img" aria-label="Instagram photo of soft blue eye makeup" style="background:#dfe7ee"></div>
  </div>
  <div class="abs handle-bar"><span class="sq"></span>@lumeandwisp</div>
</section>

<section>
  <div class="abs newsletter"></div>
  <h3 class="abs news-title">SUBSCRIBE OUR NEWSLETTER</h3>
  <p class="abs news-text">Get new trends, tutorials and exclusive offers sent straight to your inbox every week.</p>
  <div class="abs news-input"></div>
  <svg class="abs news-arrow" width="22" height="14" viewBox="0 0 22 14"><path d="M1 7h19M14 1l6 6-6 6" fill="none" stroke="#fff" stroke-width="1.6"/></svg>
</section>

<footer>
  <div class="abs footer"></div>
  <div class="abs footer-logo">Lume &amp; Wisp</div>
  <nav class="abs footer-links"><span>ABOUT US</span><span>CONTACT US</span><span>BLOG</span><span>OUR SERVICES</span><span>FAQ</span><span>PACKAGES</span></nav>
  <div class="abs social"><span></span><span></span><span></span><span></span></div>
  <div class="abs rule"></div>
  <p class="abs copyright">Copyrights 2016 | ALL RIGHTS RESERVED</p>
</footer>

</body>
</html>
```